Internaitnal Logistics Company Needs Marketing Flyer for Australia/Italy Service

TR Logistics in Australia needs an email marketing brochure to promote our international freight and logistics services between Australia and Italy. We provide Air, Sea and Trucking services to importers and exporters on this trade route. We are looking to grow our business and want to send targetted emails to companies prior to a joint sales initiative between out Italian agent and oursleves in March. Please choose the lgoo you feel is most appropriate either is fine.

I require two brochures if it isn't feasible to fit it all into 1. The attached spreadhseet shows FCL and LCL pricing which need to be seperated from each toehr as they are different types of services. Both services are containerised sea freight services please do not include Air in these flyers. All information for both FCL and LCL services that I need in the flyers is attached in the excel document and split across two worksheets.

The ultimate goal is to send these as an email attachment, happy for multiple pages if it isn't clear on 1. Please advise if any questions. Our website for more background is www.trlogistics-example.com.au.

Target Market(s)

Business 2 Business, targeting business owners or supply chain/logistics managers, target companies are importers of general cargo such as furniture, ceramics, building materials and white goods between Italy to Australia.

Industry/Entity Type

It Company

Font styles to use
Sans Serif

Colors
0555a3
3176b5
85abd2
ec1f27
f04a50
f78f20
faa54b
fbc994

Requirements
Must have
• Incorporate our service strengths and commitments from the word document. Incorporate all our service details and pricing as stated in the excel documents.
• Incorporate one of our logo's it is up to the designer how they manage this.
Nice to have
• Interested to see a mix of vectors and images.
Should not have
• Mention of airfreight or warehousing

```html
<!DOCTYPE html>
<html lang="en">
<head>
<meta charset="utf-8">
<title>TR Logistics – Italy/Australia Sea Freight Flyers</title>
<link rel="stylesheet" href="https://fonts.googleapis.com/css2?family=Oswald:wght@400;500&family=Open+Sans:wght@400;600;700&family=Roboto+Condensed:wght@400;700&display=swap">
<style>
:root{
  --navy:#23305f;
  --navy-dark:#1c2750;
  --orange:#f26a21;
  --orange-light:#faa54b;
  --red:#ec1f27;
  --sky-top:#a9d3ef;
  --sky-low:#dbeefa;
  --sea:#3a78b5;
  --grey-bg:#d6d6d6;
  --ink:#2b2b2b;
  --rule:#c9c9c9;
  --white:#ffffff;
}
*{margin:0;padding:0;box-sizing:border-box}
html,body{width:1200px;height:1200px;overflow:hidden}
body{background:var(--grey-bg);position:relative;font-family:"Open Sans",Arial,sans-serif;color:var(--ink)}
.flyer{position:absolute;top:220px;width:540px;height:760px;background:var(--white);overflow:hidden}
.flyer--offer{left:30px}
.flyer--promise{left:630px}
.abs{position:absolute}
.shapes{position:absolute;left:0;top:0}
.brand-name{position:absolute;display:flex;align-items:center;gap:8px;font-family:"Open Sans",Arial,sans-serif;font-weight:700;color:var(--navy);white-space:nowrap}
.brand-dot{width:22px;height:22px;border-radius:50%;background:var(--orange)}
.section-title{position:absolute;font-family:"Open Sans",Arial,sans-serif;font-weight:400;color:var(--orange);font-size:15px;line-height:19px;text-transform:uppercase}
.feature{position:absolute;width:230px}
.feature h3{font-size:12px;font-weight:600;color:var(--navy);margin-left:34px;text-transform:uppercase}
.feature p{font-size:9.5px;line-height:12px;margin:6px 0 0 34px;color:var(--ink)}
.feature-icon{position:absolute;left:0;top:-3px;width:24px;height:24px;border-radius:50%;background:var(--orange);display:flex;align-items:center;justify-content:center}
.divider{position:absolute;left:284px;top:360px;width:1px;height:115px;background:var(--ink)}
table{border-collapse:collapse;font-family:"Roboto Condensed",Arial,sans-serif}
.tariff{position:absolute;left:14px;top:520px;width:512px;border:2px solid var(--orange);font-size:6px}
.tariff th{font-weight:700;text-align:left;padding:6px 3px;color:var(--navy);border-bottom:1px solid var(--rule)}
.tariff td{padding:5px 3px;border-left:1px solid var(--rule);border-bottom:1px solid var(--rule);white-space:nowrap}
.tariff td:first-child{border-left:none}
.footer{position:absolute;left:0;bottom:0;width:540px;background:var(--navy);color:var(--white)}
.footer h4{font-weight:400;color:var(--orange);font-size:14px;line-height:18px}
.footer small{display:block;font-size:8px;line-height:10.5px;white-space:nowrap}
.contact-line{display:flex;align-items:center;gap:6px;font-size:13px;font-weight:600;line-height:20px;white-space:nowrap}
/* promise flyer */
.headline{position:absolute;left:0;top:34px;width:540px;text-align:center}
.headline .h-white{font-family:"Oswald",sans-serif;font-weight:400;color:var(--white);font-size:33px;line-height:38px}
.headline .h-orange{font-family:"Oswald",sans-serif;font-weight:500;color:var(--orange);font-size:31px;line-height:36px;letter-spacing:.5px}
.headline .h-sub{font-family:"Open Sans",sans-serif;font-weight:600;color:var(--white);font-size:25px;line-height:34px}
.pledges{position:absolute;left:39px;top:145px;width:467px;height:127px;border:1.5px solid var(--white);border-radius:12px;padding:10px 10px 0 20px;color:var(--white);font-size:9.5px;line-height:12.5px}
.pledges p{position:relative;margin-bottom:8px}
.pledges .q{color:var(--orange);font-size:13px;position:absolute;left:-10px;top:-4px}
.pledges .qe{color:var(--orange);font-size:11px}
.website{position:absolute;right:48px;top:290px;text-align:right;color:var(--orange);font-weight:600;white-space:nowrap}
.website .label{font-size:14px}
.website .url{font-size:13px;margin-top:4px;display:flex;align-items:center;gap:5px;justify-content:flex-end}
.rate{position:absolute;border:2px solid var(--orange);font-size:8px;background:var(--white)}
.rate th{font-weight:700;color:var(--navy);padding:6px 5px;border-bottom:1px solid var(--rule);text-align:left;white-space:nowrap}
.rate td{padding:4px 5px;border-bottom:1px solid var(--rule);border-left:1px solid var(--rule);white-space:nowrap}
.rate td:first-child{border-left:none}
.rate tr:last-child td{border-bottom:none}
.notes{position:absolute;font-family:"Roboto Condensed",Arial,sans-serif;font-size:8.5px;line-height:12.5px}
.notes h5{color:var(--orange);font-family:"Open Sans",sans-serif;font-weight:400;font-size:10.5px;margin-bottom:3px}
.contact-tab{position:absolute;left:0;top:654px;height:28px;width:150px;background:var(--orange);color:var(--white);font-size:14px;font-weight:600;padding:5px 0 0 36px;clip-path:polygon(0 0,88% 0,100% 100%,0 100%)}
.office{position:absolute;color:var(--white);font-size:8px;line-height:11px;font-weight:600;white-space:nowrap}
.office h6{color:var(--orange);font-size:10px;font-weight:600;margin-bottom:8px}
.office .cols{display:flex;gap:28px}
.office .row{display:flex;align-items:center;gap:4px}
</style>
</head>
<body>

<!-- Flyer 1: service offering and FCL tariff -->
<section class="flyer flyer--offer">
  <svg class="shapes" width="540" height="760" viewBox="0 0 540 760">
    <defs>
      <linearGradient id="oband" x1="0" x2="1"><stop offset="0" stop-color="#f26a21"/><stop offset="1" stop-color="#faa54b"/></linearGradient>
    </defs>
    <polygon points="0,280 470,300 420,318 0,305" fill="url(#oband)"/>
    <polygon points="420,318 540,255 540,272 440,318" fill="var(--navy)"/>
  </svg>
  <svg class="shapes" width="540" height="300" viewBox="0 0 540 300" role="img" aria-label="Photograph of a loaded container ship sailing at sea under a clear blue sky">
    <defs>
      <linearGradient id="sky" x1="0" y1="0" x2="0" y2="1">
        <stop offset="0" stop-color="var(--sky-top)"/><stop offset=".7" stop-color="var(--sky-low)"/><stop offset=".72" stop-color="var(--sea)"/><stop offset="1" stop-color="#7fb0d8"/>
      </linearGradient>
    </defs>
    <polygon points="0,78 300,78 336,0 540,0 540,240 470,280 0,280" fill="url(#sky)"/>
  </svg>
  <div class="brand-name" style="left:62px;top:30px;font-size:27px"><span class="brand-dot"></span>TR Logistics</div>

  <h2 class="section-title" style="left:62px;top:322px">Italy/Australia Service<br>Offering</h2>

  <div class="feature" style="left:36px;top:366px">
    <span class="feature-icon"><svg width="12" height="12" viewBox="0 0 12 12"><path d="M2 5h2v6H2zM5 5l2-4c1 0 1.5.6 1.3 1.6L8 4.5h2.4c.6 0 1 .6.9 1.2l-.9 4.4c-.1.5-.5.9-1 .9H5z" fill="#fff"/></svg></span>
    <h3>Reliable:</h3>
    <p>Market leading service offering with over 30 years' experience in Italy.</p>
  </div>
  <div class="feature" style="left:36px;top:418px">
    <span class="feature-icon"><svg width="14" height="10" viewBox="0 0 14 10"><ellipse cx="7" cy="5" rx="6" ry="4" fill="none" stroke="#fff" stroke-width="1.3"/><circle cx="7" cy="5" r="1.8" fill="#fff"/></svg></span>
    <h3>Visible:</h3>
    <p>Market leading information systems ensure you are kept up to date every step of the way with automated alerts and reporting, driving end to end performance.</p>
  </div>
  <div class="divider"></div>
  <div class="feature" style="left:306px;top:366px">
    <span class="feature-icon"><svg width="12" height="12" viewBox="0 0 12 12"><circle cx="6" cy="6" r="1.6" fill="#fff"/><circle cx="2" cy="2" r="1.2" fill="#fff"/><circle cx="10" cy="2" r="1.2" fill="#fff"/><circle cx="2" cy="10" r="1.2" fill="#fff"/><circle cx="10" cy="10" r="1.2" fill="#fff"/><path d="M2 2l8 8M10 2L2 10" stroke="#fff" stroke-width=".8"/></svg></span>
    <h3>Strong:</h3>
    <p>Market leading service offering with over 30 years' experience in Italy.</p>
  </div>
  <div class="feature" style="left:306px;top:422px">
    <span class="feature-icon"><svg width="12" height="12" viewBox="0 0 12 12"><rect x="1" y="1" width="4" height="4" fill="none" stroke="#fff"/><rect x="7" y="1" width="4" height="4" fill="none" stroke="#fff"/><rect x="1" y="7" width="4" height="4" fill="none" stroke="#fff"/><rect x="7" y="7" width="4" height="4" fill="none" stroke="#fff"/></svg></span>
    <h3>Efficient:</h3>
    <p>consolidation hubs through Italy, TR Logistics drives efficiency into your supply chain</p>
  </div>

  <h2 class="section-title" style="left:62px;top:498px;text-transform:none">ITALY to AUSTRALIA PRICING TARIFF</h2>
  <table class="tariff">
    <tr><th>CARRIER</th><th>POL</th><th>POD</th><th>20'</th><th>40'</th><th>BAF (1)</th><th>BAF (1)</th><th>ADEN/SUEZ (1)</th><th>CSF</th><th>THC (2)</th><th>ISPS</th><th>LOLO</th><th>VALIDITY</th><th>NOTES</th></tr>
    <tr><td>ORL</td><td>LA SPEZIA</td><td>SYDNEY</td><td>USD 650.00</td><td>USD 1,300.00</td><td>USD 400.00</td><td>USD 400.00</td><td>USD 90.00</td><td>USD 11.00</td><td>EUR 170.00</td><td>EUR 15.00</td><td>EUR 30.00</td><td>31-Mar</td><td>DIRECT</td></tr>
    <tr><td>BLX</td><td>GENOA</td><td>SYDNEY</td><td>USD 700.00</td><td>USD 1,400.00</td><td>INCL</td><td>INCL</td><td>INCL</td><td>INCL</td><td>EUR 172.00</td><td>EUR 15.00</td><td>EUR 30.00</td><td>28-Feb</td><td>VIA PORT KELANG</td></tr>
    <tr><td>KTS</td><td>GENOA/LA SPEZIA</td><td>SYDNEY</td><td>USD 525.00</td><td>USD 1,050.00</td><td>INCL</td><td>INCL</td><td>INCL</td><td>INCL</td><td>EUR 178.00</td><td>EUR 15.00</td><td>EUR 30.00</td><td>28-Feb</td><td>VIA PORT KELANG</td></tr>
    <tr><td>VMR</td><td>GENOA</td><td>SYDNEY</td><td>USD 600.00</td><td>USD 1,200.00</td><td>USD 389.00</td><td>USD 389.00</td><td>USD 119.00</td><td>USD 13.00</td><td>EUR 178.00</td><td>EUR 15.00</td><td>EUR 30.00</td><td>31-Mar</td><td>DIRECT</td></tr>
    <tr><td>ZDL</td><td>GENOA/LA SPEZIA</td><td>SYDNEY</td><td>USD 750.00</td><td>USD 1,325.00</td><td>INCL</td><td>INCL</td><td>INCL</td><td>INCL</td><td>EUR 180.00</td><td>EUR 15.00</td><td>EUR 30.00</td><td>28-Feb</td><td>VIA SINGAPORE</td></tr>
  </table>

  <footer class="footer" style="height:92px">
    <div class="abs" style="left:40px;top:12px">
      <h4>Notes</h4>
      <small>(1) = per TEU</small>
      <small>(2) = per Container</small>
      <small>BAF = February and is subject ot change in line with carrier changes</small>
      <small>Valid for general cargo only, HAZ will attract additional charges</small>
    </div>
    <div class="abs" style="left:300px;top:14px;width:1px;height:62px;background:var(--white)"></div>
    <div class="abs" style="left:314px;top:12px">
      <h4>Contact Us</h4>
      <div class="contact-line" style="margin-top:4px"><svg width="11" height="11" viewBox="0 0 12 12"><path d="M3 1l2 3-1.3 1.2c.7 1.4 1.7 2.4 3.1 3.1L8 7l3 2-1 2C5 11 1 7 1 2z" fill="var(--orange)"/></svg>61 7-3000-0100</div>
      <div class="contact-line" style="font-size:11.5px"><svg width="11" height="11" viewBox="0 0 12 12"><circle cx="6" cy="6" r="5" fill="none" stroke="var(--orange)" stroke-width="1.4"/><path d="M1 6h10M6 1c2 2.5 2 7.5 0 10M6 1c-2 2.5-2 7.5 0 10" stroke="var(--orange)" fill="none"/></svg>www.trlogistics-example.com.au.</div>
    </div>
  </footer>
</section>

<!-- Flyer 2: commitments, local and LCL charges -->
<section class="flyer flyer--promise">
  <svg class="shapes" width="540" height="760" viewBox="0 0 540 760">
    <defs>
      <linearGradient id="oband2" x1="0" x2="1"><stop offset="0" stop-color="#f26a21"/><stop offset="1" stop-color="#faa54b"/></linearGradient>
    </defs>
    <rect x="0" y="0" width="540" height="372" fill="var(--navy)"/>
    <polygon points="0,300 540,365 0,412" fill="var(--white)"/>
    <polygon points="0,412 540,352 540,372 0,420" fill="url(#oband2)"/>
    <rect x="0" y="680" width="540" height="80" fill="var(--navy)"/>
  </svg>

  <div class="headline">
    <div class="h-white">WE CHALLENGE INDUSTRY</div>
    <div class="h-orange">CONCEPTS AND INNOVATE IDEAS</div>
    <div class="h-sub">So you can focus on business...</div>
  </div>

  <div class="pledges">
    <p><span class="q">&ldquo;</span>We commit to creating solutions and services that are designed around your priorities, individually tailored and simple to implement, with a focus on cost reduction, convenience, visibility and risk management.<span class="qe">&rdquo;</span></p>
    <p><span class="q">&ldquo;</span>We commit to delivering operational excellence with outstanding customer service, by taking ownership and following through on our promises.<span class="qe">&rdquo;</span></p>
    <p><span class="q">&ldquo;</span>We commit to one-point-of-contact – a dedicated supply chain specialist managing your orders end to end.<span class="qe">&rdquo;</span></p>
  </div>

  <div class="brand-name" style="left:36px;top:330px;font-size:26px"><span class="brand-dot"></span>TR Logistics</div>

  <div class="website">
    <div class="label">Our Website</div>
    <div class="url">www.trlogistics-example.com.au<svg width="10" height="10" viewBox="0 0 12 12"><circle cx="6" cy="6" r="5" fill="none" stroke="var(--orange)" stroke-width="1.4"/><path d="M1 6h10M6 1c2 2.5 2 7.5 0 10M6 1c-2 2.5-2 7.5 0 10" stroke="var(--orange)" fill="none"/></svg></div>
  </div>

  <table class="rate" style="left:28px;top:430px;width:240px">
    <tr><th style="width:42%"></th><th style="text-align:center">RATE</th></tr>
    <tr><td>Port Charges*</td><td style="text-align:center">AUD 595 per 20' / AUD 685 per 40'</td></tr>
    <tr><td>Doc Fee</td><td style="text-align:center">AUD 95 per B/L</td></tr>
    <tr><td>Sea Cargo Automation</td><td style="text-align:center">AUD 20 per B/L</td></tr>
    <tr><td>Customs Clearance</td><td style="text-align:center">AUD 95 per B/L</td></tr>
    <tr><td>CMR/ICS</td><td style="text-align:center">AUD 10 per B/L</td></tr>
    <tr><td>Delivery Metro</td><td style="text-align:center">On Application</td></tr>
  </table>

  <table class="rate" style="left:290px;top:398px;width:222px">
    <tr><th>ORIGIN CHARGE</th><th>RATE</th><th>COMMENTS</th></tr>
    <tr><td>export customs</td><td>eur 80.00</td><td>refer (3) below</td></tr>
    <tr><td>port taxes</td><td>eur 1.10</td><td>per tonne</td></tr>
    <tr><td>gate in fee</td><td>eur 15.00</td><td>per container</td></tr>
    <tr><td>b/l fee</td><td>eur 70.00</td><td>per set</td></tr>
  </table>

  <table class="rate" style="left:290px;top:504px;width:222px">
    <tr><th>CONSOLIDATIONS (FCX)</th><th>RATE</th><th>COMMENTS</th></tr>
    <tr><td>container stuffing</td><td>eur 280.00</td><td>per container</td></tr>
    <tr><td>transport to wharf</td><td>eur 180.00</td><td>per container</td></tr>
  </table>

  <div class="notes" style="left:36px;top:582px;width:215px">
    <h5>Notes</h5>
    *Melbourne attracts an additional AUD38/76 per 20'/40' for Port Arbitrary All shipments are subject to duty/gst as required by law .
  </div>
  <div class="notes" style="left:296px;top:584px;width:222px">
    <h5>Notes</h5>
    One container per Export Declaration, additional container on same declaration EUR30 per container. Above rates are for general cargo only, reefer and hazardous will attract additional charges.<br>Reefer THC is EUR250 per container
  </div>

  <div class="contact-tab">Contact Us</div>

  <div class="office" style="left:36px;top:692px">
    <h6>BRISBANE (Head Office)</h6>
    <div class="cols">
      <div><div class="row"><svg width="7" height="7" viewBox="0 0 12 12"><path d="M3 1l2 3-1.3 1.2c.7 1.4 1.7 2.4 3.1 3.1L8 7l3 2-1 2C5 11 1 7 1 2z" fill="var(--orange)"/></svg>61 7 3000 0100</div><div class="row"><svg width="7" height="7" viewBox="0 0 12 12"><rect x="1" y="4" width="10" height="6" fill="var(--orange)"/></svg>61 7 3000 0177</div></div>
      <div class="row" style="align-items:flex-start"><svg width="7" height="9" viewBox="0 0 10 14"><path d="M5 0a5 5 0 015 5c0 4-5 9-5 9S0 9 0 5a5 5 0 015-5z" fill="var(--orange)"/></svg><div>Level 6 / 12 Harbour Street<br>Brisbane QLD 4000</div></div>
    </div>
  </div>
  <div class="abs" style="left:266px;top:694px;width:1px;height:50px;background:var(--white)"></div>
  <div class="office" style="left:296px;top:692px">
    <h6>SYDNEY</h6>
    <div class="cols">
      <div><div class="row"><svg width="7" height="7" viewBox="0 0 12 12"><path d="M3 1l2 3-1.3 1.2c.7 1.4 1.7 2.4 3.1 3.1L8 7l3 2-1 2C5 11 1 7 1 2z" fill="var(--orange)"/></svg>61 2 9000 0369</div><div class="row"><svg width="7" height="7" viewBox="0 0 12 12"><rect x="1" y="4" width="10" height="6" fill="var(--orange)"/></svg>61 2 9000 0370</div></div>
      <div class="row" style="align-items:flex-start"><svg width="7" height="9" viewBox="0 0 10 14"><path d="M5 0a5 5 0 015 5c0 4-5 9-5 9S0 9 0 5a5 5 0 015-5z" fill="var(--orange)"/></svg><div>Unit 5 / 48 Dock Road<br>Alexandria NSW 2015</div></div>
    </div>
  </div>
</section>

</body>
</html>
```